Awesome ecommerce store banner needed!

We need a sharp, clear, strong banner for one of our subcategory pages on http://www.brixmolt.com
We'd like to incorporate the following image. We'd like the background to be gray or black. We are replacing the Wireless Intercoms banner that is orange (we hate it).
WE do like our other banners, however, so please use them as reference:
SIze: 980 x 380
Two raw images of the intercom we'd like you to encorporate have been included. Choose one or the other depending on what you think would be best. If using the single angle, please duplicate it. We want two intercoms in the banner
Simple and Clean is key:
Text: Wireless Intercoms
Text Color: Can be white/off gray
Text Style: Please keep it clean in line with the website
Background: Black/gray/white

```html
<!DOCTYPE html>
<html lang="en">
<head>
<meta charset="utf-8">
<title>Brixmolt – Wireless Intercom Systems</title>
<link href="https://fonts.googleapis.com/css2?family=Roboto:wght@400;500;700;900&display=swap" rel="stylesheet">
<style>
  :root {
    --page-top: #e3e3e3;
    --page-bottom: #ffffff;
    --ink: #222222;
    --ink-soft: #555555;
    --ink-mute: #777777;
    --accent: #e8732a;
    --cart-red: #c8281e;
    --sale-red: #d0322a;
    --nav-top: #454545;
    --nav-bottom: #1f1f1f;
    --panel: #f0f0f0;
    --line: #cfcfcf;
    --banner-dark: #2f2d2b;
    --banner-mid: #4a4744;
    --headline-grey: #cbc7c2;
    --white: #ffffff;
  }
  html, body {
    margin: 0;
    padding: 0;
    width: 1200px;
    height: 633px;
    overflow: hidden;
    background: var(--page-bottom);
  }
  .page {
    position: relative;
    width: 1366px;
    height: 720px;
    transform: scale(0.8785);
    transform-origin: 0 0;
    overflow: hidden;
    background: linear-gradient(var(--page-top), #f2f2f2 60%, var(--page-bottom));
    font-family: "Roboto", sans-serif;
    color: var(--ink);
  }
  .abs { position: absolute; white-space: nowrap; margin: 0; }

  /* header */
  .util-links { left: 850px; top: 9px; font-size: 12px; font-weight: 700; color: var(--ink-soft); }
  .util-links span { padding: 0 10px; border-left: 1px solid #bbb; }
  .util-links span:first-child { padding-left: 0; border-left: 0; }
  .cart-btn { left: 1032px; top: 2px; width: 48px; height: 31px; background: var(--cart-red); border-radius: 0 0 3px 3px; }
  .cart-label { left: 1085px; top: 9px; font-size: 13px; font-weight: 700; color: #444; }
  .brand { left: 185px; top: 28px; display: flex; align-items: center; gap: 12px; }
  .brand__mark { width: 58px; height: 58px; border-radius: 50%; background: var(--accent); }
  .brand__name { font-size: 52px; font-weight: 900; color: #333; letter-spacing: -1px; }
  .call { right: 204px; top: 48px; font-size: 20px; color: var(--ink-soft); }
  .call strong { font-size: 25px; font-weight: 700; }
  .hours { right: 204px; top: 72px; font-size: 15px; color: var(--ink-mute); letter-spacing: 0.5px; }

  /* nav */
  .nav { left: 185px; top: 102px; width: 980px; height: 38px; background: linear-gradient(var(--nav-top), var(--nav-bottom)); }
  .nav__item { top: 8px; font-size: 19px; font-weight: 500; color: var(--white); }
  .nav__sep { top: 0; width: 1px; height: 38px; background: #111; box-shadow: 1px 0 0 #555; }
  .search { left: 630px; top: 6px; width: 346px; height: 27px; background: var(--white); border-radius: 2px; }
  .search__hint { left: 8px; top: 6px; font-size: 13px; color: #888; }
  .search__btn { right: 0; top: 0; width: 88px; height: 27px; background: linear-gradient(#f4f4f4, #d8d8d8); }
  .search__btn-text { left: 7px; top: 5px; font-size: 15px; font-weight: 700; color: #333; }

  /* content shell */
  .content { left: 185px; top: 145px; width: 980px; height: 580px; background: var(--white); }
  .sidebar { left: 185px; top: 172px; width: 213px; height: 560px; background: var(--panel); box-shadow: 2px 0 3px rgba(0,0,0,0.12); }
  .sidebar__title { left: 16px; top: 10px; font-size: 21px; font-weight: 700; color: var(--accent); }
  .sidebar__list { left: 18px; top: 62px; list-style: none; padding: 0; font-size: 12px; font-weight: 700; line-height: 15px; }
  .sidebar__list li { position: relative; padding-left: 7px; margin-bottom: 10px; }
  .sidebar__list li::before { content: ""; position: absolute; left: 0; bottom: 4px; width: 3px; height: 3px; background: var(--accent); }
  .shop-link { width: 213px; text-align: center; font-weight: 700; line-height: 1; }
  .shop-link__or { display: block; font-size: 20px; color: var(--accent); }
  .shop-link__or small { font-size: 16px; }
  .shop-link__target { display: block; font-size: 19px; color: var(--ink); margin-top: 0; }
  .shop-link__target b { color: var(--accent); }
  .sidebar__rule { left: 0; top: 410px; width: 213px; height: 1px; background: #ddd; }
  .sidebar__testimonials { left: 13px; top: 462px; font-size: 17px; font-weight: 700; }

  /* main */
  .crumbs { left: 420px; top: 171px; font-size: 13px; color: #444; }
  .crumbs .sep { color: #999; padding: 0 5px; }
  .crumbs .current { color: var(--accent); font-weight: 700; }
  .page-title { left: 420px; top: 197px; font-size: 16px; font-weight: 500; }
  .page-rule { left: 420px; top: 223px; width: 725px; height: 1px; background: #aaa; }

  .banner { left: 425px; top: 247px; width: 721px; height: 281px; overflow: hidden;
    background: radial-gradient(ellipse at 35% 40%, var(--banner-mid) 0%, var(--banner-dark) 75%); }
  .banner__top { left: 33px; top: 19px; font-size: 81px; font-weight: 700; color: var(--headline-grey); letter-spacing: 0; }
  .banner__bottom { left: 42px; top: 99px; font-size: 60px; font-weight: 700; color: var(--white); }
  .banner__product { left: 435px; top: 0; width: 286px; height: 281px;
    background: linear-gradient(160deg, rgba(185,183,179,0.12) 0%, rgba(185,183,179,0.5) 50%, rgba(20,20,20,0.8) 100%); }

  .card { top: 577px; width: 174px; height: 160px; border: 1px solid var(--line); background: var(--white); }
  .card__photo { left: 30px; top: 20px; width: 114px; height: 120px; background: linear-gradient(#d9d9d9, #9a9a9a); }
  .tag { top: 574px; height: 23px; width: 122px; font-size: 15px; font-weight: 500; color: var(--white);
    clip-path: polygon(0 0, 90% 0, 100% 100%, 0 100%); }
  .tag span { position: absolute; left: 32px; top: 3px; }
  .tag--pick { left: 600px; background: var(--accent); }
  .tag--sale { left: 966px; background: var(--sale-red); }
</style>
</head>
<body>
<div class="page">
  <div class="abs content"></div>

  <p class="abs util-links"><span>Home</span><span>About</span><span>Contact</span></p>
  <div class="abs cart-btn">
    <svg width="48" height="31" viewBox="0 0 48 31" aria-hidden="true">
      <path d="M14 8h4l3 11h11l3-8H19" fill="none" stroke="#fff" stroke-width="2.5" stroke-linejoin="round"/>
      <circle cx="22" cy="23" r="2" fill="#fff"/><circle cx="31" cy="23" r="2" fill="#fff"/>
    </svg>
  </div>
  <p class="abs cart-label">YOUR CART</p>

  <div class="abs brand"><span class="brand__mark"></span><span class="brand__name">Brixmolt</span></div>
  <p class="abs call">Call Us <strong>555.014.2290</strong></p>
  <p class="abs hours">Monday-Friday 7am-3pm PST</p>

  <nav class="abs nav">
    <span class="abs nav__item" style="left:20px">Shop Home Automation ⌄</span>
    <span class="abs nav__sep" style="left:270px"></span>
    <span class="abs nav__item" style="left:289px">Shop Cool Gadgets ⌄</span>
    <span class="abs nav__sep" style="left:496px"></span>
    <span class="abs nav__item" style="left:512px">Top Sellers</span>
    <div class="abs search">
      <span class="abs search__hint">Enter Keyword or Item#</span>
      <div class="abs search__btn"><span class="abs search__btn-text">SEARCH <b style="color:var(--accent)">›</b></span></div>
    </div>
  </nav>

  <aside class="abs sidebar">
    <p class="abs sidebar__title">Home Automation</p>
    <ul class="abs sidebar__list">
      <li>Wireless Driveway Alarm<br>Systems &amp; Outdoor Motion<br>Detectors</li>
      <li>Wireless Doorbell Systems</li>
      <li>Indoor Motion Sensors</li>
      <li>Remote Light Switches &amp;<br>Wireless Power Outlet Triggers</li>
    </ul>
    <p class="abs shop-link" style="left:0;top:230px"><span class="shop-link__or"><small>or</small> SHOP</span><span class="shop-link__target">Home Automation <b>›</b></span></p>
    <p class="abs shop-link" style="left:0;top:314px"><span class="shop-link__or"><small>or</small> SHOP</span><span class="shop-link__target" style="font-size:22px">Cool Gadgets <b>›</b></span></p>
    <div class="abs sidebar__rule"></div>
    <p class="abs sidebar__testimonials">Customer Testimonials</p>
  </aside>

  <p class="abs crumbs">Home<span class="sep">&gt;</span>View All Categories...<span class="sep">&gt;</span><span class="current">Wireless Intercom Systems</span></p>
  <h2 class="abs page-title">Wireless Intercom Systems</h2>
  <div class="abs page-rule"></div>

  <section class="abs banner">
    <div class="abs banner__product" role="img" aria-label="Two silver and black wireless intercom units with antennas, one in front of the other"></div>
    <h1 class="abs banner__top">WIRELESS</h1>
    <p class="abs banner__bottom">INTERCOMS</p>
  </section>

  <div class="abs card" style="left:420px"><div class="abs card__photo" role="img" aria-label="Wireless intercom product photo"></div></div>
  <div class="abs card" style="left:603px"><div class="abs card__photo" role="img" aria-label="Pair of intercom units product photo"></div></div>
  <div class="abs card" style="left:786px"><div class="abs card__photo" role="img" aria-label="Black intercom handset product photo"></div></div>
  <div class="abs card" style="left:969px"><div class="abs card__photo" role="img" aria-label="Intercom and door unit product photo"></div></div>
  <div class="abs tag tag--pick"><span>staff pick</span></div>
  <div class="abs tag tag--sale"><span>on sale</span></div>
</div>
</body>
</html>
```